Power Washing Business Easy Postcard Design

We need a postcard designed for our company, which does residential power washing. We clean houses, decks, driveways and fences. The design should be understated, high end with minimalist graphics. No bubbles or wild colors. The name of the business is "tallpine power washing" which should be rendered all lower case in a san serif font. Sample files in blue or white are attached. The attached files aren't our logo, just a model. The font doesn't have to be exact and "power washing" needs to be added to it.The postcard size is the Parcel Inkly 8.64" X 5.59". The photo which is attached should fill the whole front of the card.

The text elements on the front are:
1) "tallpine power washing"- as per the attached files, can be broken into two lines

2) "Mention this card and receive a FREE standard size Deck Wash"

3) "804-317-5286"

4) "tallpinepowerwashing.com" (this font size can be smaller than the phone number.)

5)"We Clean:- Houses- Decks- Driveways- Fences"The arrangement is the text is up to you. The text should not overpower the image.

Target Market(s)

Homeowners

Industry/Entity Type

Residential

Font styles to use
Sans Serif

Requirements
Should not have
• Garish graphics

```html
<!DOCTYPE html>
<html lang="en">
<head>
<meta charset="utf-8">
<title>tallpine power washing — postcard options</title>
<link rel="stylesheet" href="https://fonts.googleapis.com/css2?family=Arimo:wght@400;700&family=Oswald:wght@400;500;700&display=swap">
<style>
:root{
  --board-dark:#2a2a2a;
  --board-mid:#5a5a5a;
  --header:#000;
  --white:#fff;
  --navy:#0d2a6e;
  --ink:#111;
  --band-blue:#1479c4;
  --coupon-red:#e0201f;
  --coupon-blue:#1546d6;
  --grass:#7dc242;
  --grass-dark:#5ea82c;
  --link-red:#d4145a;
  --sky-top:#6fa6e6;
  --sky-low:#c8d8ee;
  --house-warm:#b49a7a;
}
*{box-sizing:border-box;margin:0;padding:0}
html,body{width:1200px;height:844px;overflow:hidden}
body{
  position:relative;
  background:radial-gradient(ellipse at 50% 55%,var(--board-mid) 0%,var(--board-dark) 75%);
  font-family:Arimo,Arial,sans-serif;
}
.board-title{
  position:absolute;left:0;top:0;width:1200px;height:72px;
  background:var(--header);border-bottom:3px solid #bbb;
  color:var(--white);font:700 46px/72px Arimo,Arial,sans-serif;
  text-align:center;letter-spacing:1px;
}
.card{position:absolute;width:546px;height:352px;overflow:hidden;background:var(--white)}
.card--a{left:50px;top:92px}
.card--b{left:623px;top:92px}
.card--c{left:50px;top:461px}
.card--d{left:623px;top:461px}
.photo{position:absolute}
.photo--house{
  background:
    linear-gradient(180deg,rgba(0,0,0,0) 55%,rgba(40,70,20,.55) 85%),
    radial-gradient(ellipse at 45% 62%,#f3d79a 0%,var(--house-warm) 30%,rgba(120,110,100,0) 60%),
    linear-gradient(180deg,var(--sky-top) 0%,var(--sky-low) 55%,#6f7f62 80%,#4f7a2e 100%);
}
.photo--family{
  background:
    radial-gradient(ellipse at 50% 45%,#d9c3a8 0%,#b08a64 35%,rgba(0,0,0,0) 60%),
    linear-gradient(180deg,#a9cbe9 0%,#d5e4ef 45%,#7bb04a 72%,#5e9a34 100%);
}
.brand{font-family:Arimo,Arial,sans-serif;font-weight:700;color:var(--navy);line-height:.95;letter-spacing:-.5px}
.brand span{display:block}
.brand--light{color:var(--white)}
.headline{font-family:Oswald,sans-serif;font-weight:500;color:var(--white);text-transform:uppercase;line-height:1.12}
.checklist{list-style:none;font:700 12px/17.5px Arimo,Arial,sans-serif}
.checklist li{display:flex;align-items:center;gap:4px}
.tick{width:12px;height:12px;flex:none}
.coupon{
  position:absolute;background:var(--white);border:2px dashed var(--coupon-red);
  text-align:center;color:var(--ink);font-family:Arimo,Arial,sans-serif;
  overflow:hidden;white-space:nowrap
}
.coupon span{display:block;line-height:1}
.coupon .receive{text-align:left}
.coupon .free{color:var(--coupon-red);font-weight:700;line-height:.8;padding-top:1px}
.coupon .deck{color:var(--coupon-blue);font-weight:700;line-height:.95}
.call{font-family:Oswald,sans-serif;font-weight:700;color:var(--white);text-shadow:0 2px 3px rgba(0,0,0,.8)}
.phone{display:flex;align-items:center;gap:8px;font-family:Oswald,sans-serif;font-weight:700}
.phone svg{flex:none}
.url{font-family:Arimo,Arial,sans-serif;font-weight:700;text-transform:uppercase}
.marker{
  position:absolute;width:64px;height:64px;border-radius:50%;
  background:var(--white);border:3px solid #ccc;
  color:var(--coupon-red);font:700 50px/56px Arimo,Arial,sans-serif;text-align:center
}
</style>
</head>
<body>

<h1 class="board-title">CHOOSE THE BEST COMBINATION FOR YOU?</h1>

<svg width="0" height="0" style="position:absolute">
  <defs>
    <symbol id="tick" viewBox="0 0 12 12"><path d="M1 6.5 4.5 10 11 1.5" fill="none" stroke="#e0201f" stroke-width="2.4" stroke-linecap="round"/></symbol>
    <symbol id="handset" viewBox="0 0 40 24"><path d="M2 10c0-6 36-6 36 0v4h-9v-4c-3-2-15-2-18 0v4H2z M11 13h18l6 10H5z" fill="currentColor"/><circle cx="20" cy="18" r="2.6" fill="#fff"/></symbol>
  </defs>
</svg>

<!-- Option A -->
<section class="card card--a">
  <div class="photo photo--house" role="img" aria-label="Photograph of a lit suburban house at dusk with lawn" style="left:0;top:0;width:546px;height:352px"></div>
  <svg style="position:absolute;left:395px;top:0" width="151" height="312" viewBox="0 0 151 312"><path d="M12 0H151V312H18C46 230 58 110 12 0Z" fill="#0d2a6e"/></svg>
  <div class="brand" style="position:absolute;left:14px;top:14px;font-size:33px"><span>tallpine</span><span style="font-size:22px">power washing</span></div>
  <div class="headline" style="position:absolute;right:12px;top:14px;font-size:15.5px;text-align:right">Safe for<br>environment and<br>landscaping</div>
  <ul class="checklist" style="position:absolute;right:16px;top:81px;color:var(--white)">
    <li style="justify-content:flex-end">Houses<svg class="tick"><use href="#tick"/></svg></li>
    <li style="justify-content:flex-end">Decks<svg class="tick"><use href="#tick"/></svg></li>
    <li style="justify-content:flex-end">Driveways<svg class="tick"><use href="#tick"/></svg></li>
    <li style="justify-content:flex-end">Fences<svg class="tick"><use href="#tick"/></svg></li>
  </ul>
  <div class="coupon" style="left:428px;top:158px;width:110px;height:85px;padding:2px 4px">
    <span class="receive" style="font-size:12px">Receive a</span>
    <span class="free" style="font-size:30px">FREE</span>
    <span style="font-size:11.5px">standard size</span>
    <span class="deck" style="font-size:16px">Deck Wash</span>
    <span style="font-size:11px">with this card</span>
  </div>
  <div class="brand brand--light" style="position:absolute;left:412px;top:252px;font-size:21px"><span>tallpine</span><span style="font-size:13px">power washing</span></div>
  <div style="position:absolute;left:396px;top:293px;font:italic 7.5px Arimo,Arial,sans-serif;color:var(--white)">Power &amp; Safe, Effective Cleaning</div>
  <div class="call" style="position:absolute;left:14px;top:280px;font-size:25px">CALL US TODAY</div>
  <div style="position:absolute;left:0;top:310px;width:546px;height:42px;background:linear-gradient(180deg,var(--grass),var(--grass-dark))"></div>
  <div class="phone" style="position:absolute;left:18px;top:310px;font-size:31px;color:var(--ink)"><svg width="34" height="22" style="color:var(--ink)"><use href="#handset"/></svg>804-317-5286</div>
  <div class="url" style="position:absolute;left:262px;top:324px;font-size:12px;color:var(--link-red)">www.tallpinepowerwashing.com</div>
</section>

<!-- Option B -->
<section class="card card--b">
  <div class="photo photo--house" role="img" aria-label="Photograph of a lit suburban house at dusk with lawn" style="left:0;top:0;width:546px;height:352px"></div>
  <div style="position:absolute;left:0;top:318px;width:546px;height:34px;background:#050a14"></div>
  <div class="brand" style="position:absolute;right:16px;top:14px;font-size:37px;text-align:center"><span>tallpine</span><span style="font-size:23px">power washing</span></div>
  <div class="coupon" style="left:10px;top:228px;width:144px;height:112px;padding:3px 6px">
    <span class="receive" style="font-size:16px">Receive a</span>
    <span class="free" style="font-size:40px">FREE</span>
    <span style="font-size:15px">standard size</span>
    <span class="deck" style="font-size:21px">Deck Wash</span>
    <span style="font-size:15px">with this card</span>
  </div>
  <div class="call" style="position:absolute;right:14px;top:260px;font-size:22px">CALL US TODAY</div>
  <div class="phone call" style="position:absolute;right:14px;top:284px;font-size:31px"><svg width="38" height="24"><use href="#handset"/></svg>804-317-5286</div>
  <div class="url" style="position:absolute;right:16px;top:330px;font-size:13px;color:#4fb3ff">www.tallpinepowerwashing.com</div>
</section>

<!-- Option C -->
<section class="card card--c">
  <div style="position:absolute;left:0;top:0;width:546px;height:22px;background:var(--band-blue)"></div>
  <div class="photo" role="img" aria-label="Sky fading into a photograph of a lit house at dusk" style="left:0;top:22px;width:273px;height:308px;background:linear-gradient(180deg,#2e8ee0 0%,#a6ccef 45%,#c9d9ee 62%,#a69682 82%,#5b7a3a 100%)"></div>
  <div class="headline" style="position:absolute;left:14px;top:30px;font-size:24px;line-height:1.15">Safe for<br>environment and<br>landscaping</div>
  <ul class="checklist" style="position:absolute;left:16px;top:124px;color:var(--navy)">
    <li><svg class="tick"><use href="#tick"/></svg>Houses</li>
    <li><svg class="tick"><use href="#tick"/></svg>Decks</li>
    <li><svg class="tick"><use href="#tick"/></svg>Driveways</li>
    <li><svg class="tick"><use href="#tick"/></svg>Fences</li>
  </ul>
  <div style="position:absolute;left:0;top:330px;width:273px;height:22px;background:var(--grass-dark)"></div>
  <div class="url" style="position:absolute;left:6px;top:335px;font-size:11.5px;color:var(--white)">www.tallpinepowerwashing.com</div>
  <div style="position:absolute;left:272px;top:22px;width:2px;height:330px;background:#9fc6ea"></div>
  <div class="coupon" style="left:288px;top:32px;width:143px;height:112px;padding:3px 6px">
    <span class="receive" style="font-size:16px">Receive a</span>
    <span class="free" style="font-size:40px">FREE</span>
    <span style="font-size:15px">standard size</span>
    <span class="deck" style="font-size:21px">Deck Wash</span>
    <span style="font-size:15px">with this card</span>
  </div>
  <div class="brand" style="position:absolute;right:10px;top:304px;font-size:25px;text-align:center"><span>tallpine</span><span style="font-size:15px">power washing</span></div>
</section>

<!-- Option D -->
<section class="card card--d">
  <div style="position:absolute;left:0;top:0;width:546px;height:24px;background:var(--band-blue)"></div>
  <div style="position:absolute;left:0;top:24px;width:276px;height:328px;background:linear-gradient(180deg,#eef3f8 40%,#dfe7ee 100%)"></div>
  <div style="position:absolute;left:4px;top:24px;width:28px;height:328px;background:var(--navy)"></div>
  <div class="url" style="position:absolute;left:18px;top:188px;transform:translate(-50%,-50%) rotate(-90deg);white-space:nowrap;font-size:12px;color:var(--white)">www.tallpinepowerwashing.com</div>
  <div class="photo photo--family" role="img" aria-label="Photograph of a family sitting on a lawn in front of a timber house" style="left:36px;top:26px;width:232px;height:148px"></div>
  <div class="headline" style="position:absolute;left:38px;top:178px;font-size:17px;color:var(--navy);line-height:1.3">Safe for environment<br>and landscaping</div>
  <ul class="checklist" style="position:absolute;left:40px;top:222px;color:var(--navy)">
    <li><svg class="tick"><use href="#tick"/></svg>Houses</li>
    <li><svg class="tick"><use href="#tick"/></svg>Decks</li>
    <li><svg class="tick"><use href="#tick"/></svg>Driveways</li>
    <li><svg class="tick"><use href="#tick"/></svg>Fences</li>
  </ul>
  <div class="coupon" style="left:132px;top:236px;width:132px;height:104px;padding:3px 6px">
    <span class="receive" style="font-size:15px">Receive a</span>
    <span class="free" style="font-size:37px">FREE</span>
    <span style="font-size:14px">standard size</span>
    <span class="deck" style="font-size:19px">Deck Wash</span>
    <span style="font-size:14px">with this card</span>
  </div>
  <div style="position:absolute;left:276px;top:24px;width:2px;height:328px;background:#9fc6ea"></div>
  <div style="position:absolute;left:462px;top:36px;width:70px;height:68px;border:2px solid #333"></div>
  <div class="brand" style="position:absolute;right:10px;top:304px;font-size:25px;text-align:center"><span>tallpine</span><span style="font-size:15px">power washing</span></div>
</section>

<div class="marker" style="left:18px;top:264px">a</div>
<div class="marker" style="left:1135px;top:224px">b</div>
<div class="marker" style="left:18px;top:710px">c</div>
<div class="marker" style="left:1128px;top:636px">d</div>

</body>
</html>
```